Coach/consultant in conflict and challenge needs an enticing flyer

I need a double sided DL flyer design that will describe my work in helping people meet conflict and emotional challenge so they can learn and grow from these difficulties. I want to give a flavour of my style through fresh colours, repeated images used differently (the spiral), and a sense of positivity around conflict and difficulty. I want to attract people who are keen to do things differently and want to engage with creative processes rather than getting stuck in familiar patterns. My work is creative and often includes use of story, images and fables, so I want to convey that as well. I also place the work in a spiritual context, but grounded in practicality so I don't want it to seem New Age or flakey. I want something that seems innovative, professional and intriguing. I've included a sample of something I mocked up in word and also a copy of a flyer for Marla Quennet's Ember Gathering that inspired me to get a DL flyer. I want the design to communicate trust and transformation and engaging with fresh ways of doing things by moving past old habits

Target Market(s)

Mid 30s plus women and men who want to change their approach to conflict and emotional difficulties and are willing to take the creative and challenging journey to do that

Industry/Entity Type

Learn

Colors
acd136
00a990

Requirements
Must have
• a shift in the use of the spiral image,
• use of image of me (Norah)
• bright fresh colours olours that represent growth and transformation--I've suggested lime green as it suggests a sense of growth
• easy to read text
Nice to have
• Interesting non-traditional fonts perhaps text in a contemporary sans serif and another brush script font (like the Ember Gathering example)
• bleed to the edge and run off the page images or text
Should not have
• anything that represents too much tradition or stuckness

```html
<!DOCTYPE html>
<html lang="en">
<head>
<meta charset="utf-8">
<title>Norah Callander – Coach, Educator and Mediator</title>
<link rel="stylesheet" href="https://fonts.googleapis.com/css2?family=Comic+Neue:ital,wght@0,400;0,700;1,700&display=swap">
<style>
  :root {
    --frame: #3d3d3f;
    --lime-deep: #a9d45a;
    --lime-pale: #d8ecc0;
    --mist: #eef7e6;
    --leaf: #8cc978;
    --brush-dark: #6e4326;
    --brush-light: #9b6a45;
    --ink: #444446;
    --ink-strong: #1f1f1f;
    --marker: #d8452d;
  }
  * { margin: 0; padding: 0; box-sizing: border-box; }
  html, body {
    width: 1200px; height: 635px; overflow: hidden;
    background: #ffffff;
    font-family: "Comic Neue", "Comic Sans MS", sans-serif;
  }
  .sheet {
    position: absolute; left: 26px; top: 26px;
    width: 1148px; height: 584px;
    background: var(--frame);
  }
  .flyer {
    position: absolute; left: 41px; top: 40px;
    width: 1066px; height: 502px;
    border: 1px solid #222;
    overflow: hidden;
    background:
      radial-gradient(ellipse 45% 55% at 8% 12%, var(--lime-deep) 0%, transparent 70%),
      radial-gradient(ellipse 35% 45% at 55% 10%, var(--mist) 0%, transparent 75%),
      radial-gradient(ellipse 40% 50% at 40% 85%, var(--mist) 0%, transparent 70%),
      radial-gradient(ellipse 45% 60% at 98% 90%, var(--leaf) 0%, transparent 70%),
      radial-gradient(ellipse 30% 40% at 90% 20%, #c9e6b8 0%, transparent 75%),
      linear-gradient(135deg, var(--lime-pale) 0%, #cfe9c4 50%, #a8d89a 100%);
  }
  .brush-artwork {
    position: absolute; left: 96px; top: 144px;
    width: 205px; height: 193px;
    border-radius: 18px;
    background: radial-gradient(ellipse at 50% 50%, var(--brush-light) 0%, var(--brush-dark) 100%);
    opacity: 0.55;
  }
  .contact {
    position: absolute; left: 26px; top: 370px;
    width: 340px; text-align: center;
    color: var(--ink); font-size: 15px; line-height: 17.7px;
  }
  .contact .name {
    color: var(--ink-strong); font-size: 19px; line-height: 22px;
  }
  .copy {
    position: absolute; left: 372px; top: 44px; width: 660px;
    color: var(--ink);
  }
  .intro {
    font-weight: 700; font-style: italic;
    font-size: 16.8px; line-height: 26px; letter-spacing: 0.3px;
  }
  .body {
    font-size: 17.4px; line-height: 29.4px; margin-top: 22px;
  }
  .body + .body { margin-top: 25px; }
  .services {
    list-style: none; margin-top: 22px;
    font-size: 17.4px; line-height: 28.6px; letter-spacing: 0.3px;
  }
  .services li { position: relative; padding-left: 31px; }
  .services li::before {
    content: ""; position: absolute; left: 2px; top: 9px;
    border-left: 11px solid var(--marker);
    border-top: 5.5px solid transparent;
    border-bottom: 5.5px solid transparent;
  }
</style>
</head>
<body>
  <div class="sheet">
    <section class="flyer">
      <div class="brush-artwork" role="img" aria-label="Hand-painted brown brush-stroke artwork"></div>

      <div class="contact">
        <p class="name">Norah Callander</p>
        <p>PhD, MCR, BAppSci, DipHum, AssDipEd</p>
        <p>0400 555 018 (m) | +61 3 5550 1427 (h)</p>
        <p>norah@norahcallander.com | norahcallander.com</p>
        <p>ABN 12 345 678 90</p>
      </div>

      <div class="copy">
        <p class="intro">Norah Callander is a coach, educator and mediator. She works with people who want to harvest the fruits of challenge and conflict so they live life differently.</p>
        <p class="body">Consult with Norah to address challenges in your life, relationship, group or organisation. Through listening, conversation and creative processes, you will discover what your challenge is asking of you. Norah Callander is a skilled facilitator who works to shift people’s responses from reactivity to creativity.</p>
        <p class="body">With many years’ experience in coaching and mentorship, mediation and narrative processes, Norah supports you to uncover unique responses to difficult situations.</p>
        <ul class="services">
          <li>CONSULTATIONS</li>
          <li>WORKSHOPS</li>
          <li>SPEAKING</li>
          <li>ARTICLES</li>
        </ul>
      </div>
    </section>
  </div>
</body>
</html>
```